Flyer / Mailer for Business Debt Relief Business - Harborline Relief 6" x 11"

We need a 6" x 11" double sided flyer. This will be sent out to potential customers with high interest business loans. We would like the design to coordinate with the colors of our logo. I have included a mock up that we sketched out. I have also included a file of a mailer we received that we would like to use as a template (not colors or fonts, just set up). I have also included an .ai file of our logo.

```html
<!DOCTYPE html>
<html lang="en">
<head>
<meta charset="utf-8">
<title>Harborline Relief – Business Debt Relief Mailer</title>
<link rel="stylesheet" href="https://fonts.googleapis.com/css2?family=Nunito+Sans:ital,wght@0,400;0,600;0,700;0,800;1,400;1,700;1,800&display=swap">
<style>
  :root {
    --green: #76bc43;
    --blue: #0a7cc4;
    --blue-panel: #3d9fdc;
    --ink: #333333;
    --ink-soft: #555555;
    --white: #ffffff;
    --backdrop: #ececec;
  }
  * { margin: 0; padding: 0; box-sizing: border-box; }
  html, body { width: 1200px; height: 1000px; overflow: hidden; }
  body {
    background: var(--backdrop);
    font-family: "Nunito Sans", Arial, sans-serif;
    color: var(--ink);
    position: relative;
  }
  .card {
    position: absolute;
    left: 187px;
    width: 872px;
    height: 476px;
    background: var(--white);
    overflow: hidden;
  }
  .card--front { top: 14px; }
  .card--back { top: 512px; }
  .bar { position: absolute; }
  .bar--green { background: var(--green); }
  .bar--blue { background: var(--blue); }

  .brand { position: absolute; text-align: center; }
  .brand__mark { display: block; background: var(--green); }
  .brand__name {
    font-weight: 400;
    color: var(--ink);
    letter-spacing: 2px;
    text-transform: uppercase;
    white-space: nowrap;
  }

  .front-brand { left: 30px; top: 30px; width: 230px; }
  .front-brand .brand__mark { width: 56px; height: 56px; margin: 0 auto 14px; }
  .front-brand .brand__name { font-size: 19px; }

  .divider { position: absolute; left: 256px; top: 29px; width: 1.5px; height: 96px; background: #777; }

  .headline {
    position: absolute; left: 278px; top: 48px;
    font-size: 30px; font-style: italic; font-weight: 400; color: var(--ink); white-space: nowrap;
  }
  .headline strong { color: var(--blue); font-weight: 800; }
  .subline { position: absolute; left: 278px; top: 83px; font-size: 15px; color: var(--ink); white-space: nowrap; }

  .photo { position: absolute; }
  .photo--desk { left: 14px; top: 137px; width: 243px; height: 325px; background: linear-gradient(160deg, #d9d6d2 0%, #5a5550 45%, #2a2826 100%); }
  .photo--worker { left: 620px; top: 137px; width: 238px; height: 325px; background: linear-gradient(200deg, #8fb86a 0%, #c9b89f 40%, #e8e6e2 75%, #f1efec 100%); }

  .offer { position: absolute; left: 257px; top: 137px; width: 363px; height: 242px;
    background: linear-gradient(180deg, #3f9fdb 0%, #4aa8e0 60%, #3b9ad6 100%); color: var(--white); }
  .offer__kicker { position: absolute; left: 0; right: 0; top: 10px; text-align: center; font-size: 16.5px; font-style: italic; font-weight: 800; }
  .offer__title { position: absolute; left: 0; right: 0; top: 23px; text-align: center; font-size: 45px; font-weight: 800; letter-spacing: 0.5px; }
  .offer__list { position: absolute; left: 30px; top: 77px; list-style: none; }
  .offer__list li { display: flex; align-items: center; height: 16.8px; font-size: 13.4px; font-weight: 600; white-space: nowrap; }
  .offer__list svg { width: 14px; height: 14px; margin-right: 9px; flex: none; }

  .cta { position: absolute; left: 257px; top: 379px; width: 363px; height: 83px; background: var(--green); color: var(--white); text-align: center; }
  .cta__notch { position: absolute; left: 26px; top: -1px; }
  .cta__label { margin-top: 13px; font-size: 8.5px; font-weight: 600; letter-spacing: 0.2px; }
  .cta__phone { font-size: 30px; font-weight: 800; line-height: 30px; letter-spacing: 0.5px; }
  .cta__line { font-size: 11px; line-height: 12.5px; }

  .back-brand { left: 31px; top: 40px; display: flex; align-items: center; gap: 12px; text-align: left; }
  .back-brand .brand__mark { width: 46px; height: 46px; }
  .back-brand .brand__name { font-size: 19px; }
  .address { position: absolute; left: 91px; top: 90px; width: 192px; border-top: 1px solid #888; padding-top: 5px;
    font-size: 11px; font-weight: 700; line-height: 13.5px; text-transform: uppercase; color: var(--ink); }

  .back-headline { position: absolute; left: 36px; top: 158px; font-size: 21px; font-weight: 700; line-height: 27px; color: var(--ink); }
  .back-body { position: absolute; left: 36px; top: 240px; font-size: 21px; font-style: italic; line-height: 27px; color: var(--ink); }

  .postage { position: absolute; left: 753px; top: 31px; width: 86px; height: 85px; border: 1px solid #555;
    font-size: 9px; line-height: 11px; text-align: center; padding-top: 24px; text-transform: uppercase; color: var(--ink); }
</style>
</head>
<body>

<section class="card card--front" aria-label="Mailer front">
  <div class="bar bar--green" style="left:13px;top:0;width:422px;height:15px"></div>
  <div class="bar bar--green" style="left:0;top:0;width:14px;height:137px"></div>
  <div class="bar bar--blue" style="left:436px;top:462px;width:436px;height:14px"></div>
  <div class="bar bar--blue" style="left:858px;top:239px;width:14px;height:237px"></div>

  <div class="brand front-brand">
    <span class="brand__mark"></span>
    <span class="brand__name">Harborline Relief</span>
  </div>
  <div class="divider"></div>

  <h1 class="headline">Helping businesses <strong>focus on what matters!</strong></h1>
  <p class="subline">We understand that merchant cash advance loans can be a burden on your business</p>

  <div class="photo photo--desk" role="img" aria-label="Photo of a business owner counting cash at a desk with a calculator, phone and ledger"></div>

  <div class="offer">
    <p class="offer__kicker">Overwhelmed by daily/weekly payments?</p>
    <h2 class="offer__title">WE CAN HELP!</h2>
    <ul class="offer__list">
      <li><svg viewBox="0 0 14 14"><circle cx="7" cy="7" r="6" fill="none" stroke="#fff" stroke-width="1.3"/><path d="M4 7.2l2.2 2.2L10.4 4.6" fill="none" stroke="#fff" stroke-width="1.6"/></svg>This is not a loan, WE ARE NOT LENDERS!</li>
      <li><svg viewBox="0 0 14 14"><circle cx="7" cy="7" r="6" fill="none" stroke="#fff" stroke-width="1.3"/><path d="M4 7.2l2.2 2.2L10.4 4.6" fill="none" stroke="#fff" stroke-width="1.6"/></svg>Improve your business cash flow immediately</li>
      <li><svg viewBox="0 0 14 14"><circle cx="7" cy="7" r="6" fill="none" stroke="#fff" stroke-width="1.3"/><path d="M4 7.2l2.2 2.2L10.4 4.6" fill="none" stroke="#fff" stroke-width="1.6"/></svg>Move payments to one monthly amount</li>
      <li><svg viewBox="0 0 14 14"><circle cx="7" cy="7" r="6" fill="none" stroke="#fff" stroke-width="1.3"/><path d="M4 7.2l2.2 2.2L10.4 4.6" fill="none" stroke="#fff" stroke-width="1.6"/></svg>Reduce the amount you are paying out monthly</li>
      <li><svg viewBox="0 0 14 14"><circle cx="7" cy="7" r="6" fill="none" stroke="#fff" stroke-width="1.3"/><path d="M4 7.2l2.2 2.2L10.4 4.6" fill="none" stroke="#fff" stroke-width="1.6"/></svg>Strategic alternatives to high interest loans</li>
      <li><svg viewBox="0 0 14 14"><circle cx="7" cy="7" r="6" fill="none" stroke="#fff" stroke-width="1.3"/><path d="M4 7.2l2.2 2.2L10.4 4.6" fill="none" stroke="#fff" stroke-width="1.6"/></svg>Fast, confidential business debt relief</li>
      <li><svg viewBox="0 0 14 14"><circle cx="7" cy="7" r="6" fill="none" stroke="#fff" stroke-width="1.3"/><path d="M4 7.2l2.2 2.2L10.4 4.6" fill="none" stroke="#fff" stroke-width="1.6"/></svg>No-obligation consultation</li>
      <li><svg viewBox="0 0 14 14"><circle cx="7" cy="7" r="6" fill="none" stroke="#fff" stroke-width="1.3"/><path d="M4 7.2l2.2 2.2L10.4 4.6" fill="none" stroke="#fff" stroke-width="1.6"/></svg>Absolutely no credit pulls</li>
      <li><svg viewBox="0 0 14 14"><circle cx="7" cy="7" r="6" fill="none" stroke="#fff" stroke-width="1.3"/><path d="M4 7.2l2.2 2.2L10.4 4.6" fill="none" stroke="#fff" stroke-width="1.6"/></svg>No collateral, no financials</li>
    </ul>
  </div>

  <div class="cta">
    <svg class="cta__notch" width="24" height="14" viewBox="0 0 24 14"><path d="M0 0h24L12 13z" fill="#3b9ad6"/></svg>
    <p class="cta__label">CALL NOW FOR FREE CONSULTATION WITH OUR EXPERTS</p>
    <p class="cta__phone">844-555-0172</p>
    <p class="cta__line">Email: info@harborlinerelief.com</p>
    <p class="cta__line">Visit our website: www.harborlinerelief.com</p>
  </div>

  <div class="photo photo--worker" role="img" aria-label="Photo of a worker in a high-visibility vest writing on a clipboard"></div>
</section>

<section class="card card--back" aria-label="Mailer back">
  <div class="bar bar--green" style="left:13px;top:0;width:425px;height:13px"></div>
  <div class="bar bar--green" style="left:0;top:0;width:14px;height:238px"></div>
  <div class="bar bar--blue" style="left:439px;top:462px;width:433px;height:14px"></div>
  <div class="bar bar--blue" style="left:858px;top:238px;width:14px;height:238px"></div>

  <div class="brand back-brand">
    <span class="brand__mark"></span>
    <span class="brand__name">Harborline Relief</span>
  </div>
  <p class="address">1450 W. Cedar Ave,&nbsp; Suite 300<br>Arlington, TX 76011</p>

  <h2 class="back-headline">Strategic debt relief for<br>businesses of all sizes.</h2>
  <p class="back-body">Stop taking out loans to<br>pay off other loans.<br>Take back your business’s<br>cash flow, and focus on<br>what matters.</p>

  <div class="postage">PRSRT STD<br>US POSTAGE<br>PAID</div>
</section>

</body>
</html>
```